Einladungskarten-Design für Ehepaar
Zielgruppe
Wir sind ein Ehepaar und feiern 2 Geburtstage und eine Hochzeit in einem grossen Fest. Unsere Zielgruppe sind unsere Freunde.
Aufgabenstellung
Doppelkarte A5 quer, nur Frontseite designed; Briefing siehe Worddok

```html
<!DOCTYPE html>
<html lang="de">
<head>
<meta charset="utf-8">
<title>Einladung – 2x60 &amp; Hochzeit</title>
<link rel="stylesheet" href="https://fonts.googleapis.com/css2?family=Lato:wght@400;700&display=swap">
<style>
  :root {
    --backdrop: #f9d4d8;
    --paper-light: #fdf3df;
    --paper-mid: #f9e6c6;
    --paper-edge: #efd3a8;
    --ink: #5a5450;
    --rule: #efb3bb;
    --accent: #f0a2b2;
    --bloom-pink: #f08aa6;
    --bloom-orange: #f29a3c;
  }
  html, body {
    margin: 0;
    padding: 0;
    width: 856px;
    height: 1200px;
    overflow: hidden;
    background: var(--backdrop);
  }
  .canvas {
    position: relative;
    width: 856px;
    height: 1200px;
  }
  .invitation {
    position: absolute;
    left: 48px;
    top: 329px;
    width: 760px;
    height: 543px;
    display: block;
    box-shadow: 0 2px 10px rgba(120, 60, 60, 0.12);
  }
  .invitation text {
    font-family: "Lato", sans-serif;
  }
  .intro { fill: var(--ink); font-size: 25px; }
  .date { fill: var(--ink); font-size: 20px; letter-spacing: 0.5px; }
  .count { fill: var(--ink); font-size: 22px; letter-spacing: 1px; }
  .field { fill: var(--ink); font-size: 13px; }
  .hint { fill: var(--ink); font-size: 6.5px; }
  .rule { stroke: var(--rule); stroke-width: 0.9; fill: none; }
  .headline { fill: var(--accent); font-size: 118px; letter-spacing: -3px; }
  .subhead { fill: var(--accent); font-size: 54px; font-weight: 700; letter-spacing: -0.5px; }
  .tagline { fill: var(--accent); font-size: 19.5px; }
</style>
</head>
<body>
<main class="canvas">
  <svg class="invitation" viewBox="0 0 612 437" xmlns="http://www.w3.org/2000/svg" aria-label="Einladungskarte">
    <defs>
      <radialGradient id="paper" cx="45%" cy="40%" r="75%">
        <stop offset="0%" stop-color="var(--paper-light)"/>
        <stop offset="65%" stop-color="var(--paper-mid)"/>
        <stop offset="100%" stop-color="var(--paper-edge)"/>
      </radialGradient>
      <radialGradient id="bloom-rose" cx="60%" cy="40%" r="55%">
        <stop offset="0%" stop-color="var(--bloom-pink)" stop-opacity="0.95"/>
        <stop offset="55%" stop-color="#f4a0b4" stop-opacity="0.7"/>
        <stop offset="100%" stop-color="#f4a0b4" stop-opacity="0"/>
      </radialGradient>
      <radialGradient id="bloom-poppy" cx="35%" cy="65%" r="60%">
        <stop offset="0%" stop-color="var(--bloom-orange)" stop-opacity="0.95"/>
        <stop offset="55%" stop-color="#f5b256" stop-opacity="0.65"/>
        <stop offset="100%" stop-color="#f5b256" stop-opacity="0"/>
      </radialGradient>
    </defs>

    <rect class="paper" width="612" height="437" fill="url(#paper)"/>

    <rect class="bouquet bouquet--top" x="405" y="-10" width="220" height="165" fill="url(#bloom-rose)" role="img" aria-label="Aquarell-Blumenstrauß mit rosa Pfingstrosen und grünen Blättern"/>
    <rect class="bouquet bouquet--bottom" x="-10" y="262" width="215" height="185" fill="url(#bloom-poppy)" role="img" aria-label="Aquarell-Blumenstrauß mit orangen und gelben Blüten"/>

    <g class="guides">
      <polyline class="rule" points="20,95 212,95 212,48 240,48"/>
      <polyline class="rule" points="240,48 240,88 380,88 380,70"/>
      <polyline class="rule" points="380,116 298,116 298,207"/>
      <polyline class="rule" points="298,150 420,150 420,212"/>
      <polyline class="rule" points="298,152 110,152 110,190"/>
      <line class="rule" x1="110" y1="207" x2="298" y2="207"/>
      <polyline class="rule" points="110,207 48,207 48,262"/>
    </g>

    <g class="details">
      <text class="intro" x="34" y="47">Wir laden</text>
      <text class="intro" x="34" y="83">euch ein...</text>

      <text class="hint" x="214" y="44">Wann?</text>
      <text class="date" x="255" y="81">06.10.2018</text>

      <text class="hint" transform="translate(384,88) rotate(90)">Wieso?</text>
      <text class="count" x="306" y="143">6 x 10</text>

      <text class="field" x="124" y="180">Doppelgeburtstag</text>

      <text class="hint" x="50" y="203">Wo?</text>
      <text class="field" x="56" y="239">Adresse</text>
    </g>

    <g class="title">
      <text class="headline" x="286" y="323">2x60</text>
      <text class="subhead" x="286" y="374">&amp; Hochzeit</text>
      <text class="tagline" x="288" y="403">2 Geburtstage &amp; 1 Hochzeit</text>
    </g>
  </svg>
</main>
</body>
</html>
```